Cross Country Transportation and Logistics Company need a Business Card Design

We need a business Card Design for a company based in Singapore, We had offices in Malaysia, Bangkok, Vietnam and China. Our Core business is cross border trucking to and from Singapore, Malaysia and Thailand. Our service also include event logistics, show moves and freight forwarding services. We made logistics possible is the region of Intra Asia.

Detail of the company as below.
Company Name: ORBEX FREIGHT (S) PTE LTD
Company Registration Number: 208867392K
Address: 14 Tuas Berry Industrial Way 3C #05-22 TBW Cargohub Singapore 539284
Office: +65 62418397
Fax: +65 62418764
Webiste: www.orbexfreight.example.sg

Business Card holder as below:
Name: Marcus Teo
Position: Director
Mobile: +65 9847 1156
Email: marcus.teo@orbexfreight.example.sg

Name: Clara Seah
Position: Finance Manager
Mobile: +65 9312 8840
Email: clara.seah@orbexfreight.example.sg

Name: Derek Koh
Position: General Manager
Mobile: +6016 584 3927
Email: derek.koh@orbexfreight.example.sg

Target Market(s)

I am targeting on the electronic component manufacturer and their freight to transport from Singapore to Malaysia and Thailand r vice verse.

Industry/Entity Type

Freight Forwarding

Requirements
Must have
• FREIGHT ACROSS BORDERS, DONE RIGHT

```html
<!DOCTYPE html>
<html lang="en">
<head>
<meta charset="utf-8">
<title>Orbex Freight – Business Card</title>
<link href="https://fonts.googleapis.com/css2?family=Lato:wght@400;700;900&display=swap" rel="stylesheet">
<style>
  :root {
    --navy: #1b2f8f;
    --navy-soft: #2a3f9e;
    --ink: #1c1c1c;
    --paper: #f7f7f9;
    --paper-edge: #e6e7ec;
    --ghost: #dcdee6;
    --stage: #3a3a3c;
    --white: #ffffff;
  }
  * { box-sizing: border-box; margin: 0; padding: 0; }
  html, body { width: 1200px; height: 900px; overflow: hidden; }
  body {
    background: var(--stage);
    font-family: "Lato", Arial, sans-serif;
    position: relative;
  }
  .card {
    position: absolute;
    width: 540px;
    height: 320px;
    border-radius: 16px;
    background: linear-gradient(160deg, var(--white), var(--paper) 60%, var(--paper-edge));
    overflow: hidden;
    box-shadow: 0 14px 30px rgba(0,0,0,.45);
  }
  .card-front { left: 80px; top: 110px; }
  .card-back { left: 580px; top: 470px; }

  .ghost-mark {
    position: absolute;
    border-radius: 50%;
    background: var(--ghost);
    opacity: .5;
  }
  .card-front .ghost-mark { width: 170px; height: 170px; left: 40px; top: 150px; }
  .card-back .ghost-mark { width: 150px; height: 150px; right: -30px; top: 130px; }

  .wordmark {
    position: absolute;
    display: flex;
    align-items: center;
    gap: 12px;
    color: var(--navy);
    font-weight: 900;
    letter-spacing: 1px;
    white-space: nowrap;
    z-index: 1;
  }
  .wordmark-dot { border-radius: 50%; background: var(--navy); flex: none; }
  .card-front .wordmark { left: 0; right: 0; justify-content: center; top: 88px; font-size: 44px; }
  .card-front .wordmark-dot { width: 34px; height: 34px; }
  .card-back .wordmark { left: 28px; top: 126px; font-size: 28px; }
  .card-back .wordmark-dot { width: 22px; height: 22px; }

  .tagline-band {
    position: absolute;
    left: 0; right: 0; bottom: 0;
    height: 72px;
    background: var(--navy);
    display: flex;
    align-items: center;
    justify-content: center;
    color: var(--white);
    font-weight: 700;
    font-size: 14px;
    letter-spacing: 3px;
    white-space: nowrap;
  }

  .name-band {
    position: absolute;
    left: 0; right: 0; top: 0;
    height: 62px;
    background: var(--navy);
    color: var(--white);
    text-align: right;
    padding: 10px 26px 0 0;
  }
  .holder-name { font-weight: 900; font-size: 22px; letter-spacing: .5px; line-height: 1; }
  .holder-title { font-size: 11px; letter-spacing: 1px; margin-top: 4px; }

  .company-block {
    position: absolute;
    right: 26px; top: 74px;
    text-align: right;
    line-height: 1.25;
    z-index: 1;
  }
  .company-web { color: var(--navy); font-size: 12px; font-weight: 700; display: flex; justify-content: flex-end; align-items: center; gap: 5px; }
  .company-name { color: var(--ink); font-weight: 900; font-size: 15px; }
  .company-reg { color: var(--navy-soft); font-weight: 700; font-size: 12px; }

  .contact-grid {
    position: absolute;
    left: 120px; top: 192px;
    display: grid;
    grid-template-columns: 140px 260px;
    row-gap: 9px;
    column-gap: 14px;
    z-index: 1;
  }
  .contact {
    display: flex; align-items: center; gap: 7px;
    color: var(--ink); font-size: 12.5px; font-weight: 700;
    white-space: nowrap;
  }
  .icon { width: 14px; height: 14px; flex: none; fill: var(--ink); }
  .company-web .icon { width: 12px; height: 12px; }

  .address {
    position: absolute;
    left: 26px; right: 20px; bottom: 20px;
    display: flex; align-items: center; gap: 9px;
    color: var(--ink); font-size: 13px; font-weight: 700;
    white-space: nowrap;
    z-index: 1;
  }
</style>
</head>
<body>

  <section class="card card-front" aria-label="Business card front">
    <div class="ghost-mark" aria-hidden="true"></div>
    <div class="wordmark"><span class="wordmark-dot"></span>ORBEX FREIGHT</div>
    <div class="tagline-band">FREIGHT ACROSS BORDERS, DONE RIGHT</div>
  </section>

  <section class="card card-back" aria-label="Business card back">
    <div class="ghost-mark" aria-hidden="true"></div>

    <header class="name-band">
      <div class="holder-name">MARCUS TEO</div>
      <div class="holder-title">DIRECTOR</div>
    </header>

    <div class="company-block">
      <div class="company-web">
        <svg class="icon" viewBox="0 0 16 16" aria-hidden="true"><path d="M6.5 9.5l3-3M5 8l-2 2a2.1 2.1 0 003 3l2-2M11 8l2-2a2.1 2.1 0 00-3-3L8 5" fill="none" style="stroke:var(--navy)" stroke-width="1.8"/></svg>
        www.orbexfreight.example.sg
      </div>
      <div class="company-name">ORBEX FREIGHT (S) PTE LTD</div>
      <div class="company-reg">Registration Number: 208867392K</div>
    </div>

    <div class="wordmark"><span class="wordmark-dot"></span>ORBEX FREIGHT</div>

    <div class="contact-grid">
      <div class="contact">
        <svg class="icon" viewBox="0 0 16 16" aria-hidden="true"><path d="M1 5c0-2 3-3 7-3s7 1 7 3v1h-3V5H4v1H1zM4 7h8l2 6H2z"/></svg>
        +65 62418397
      </div>
      <div class="contact">
        <svg class="icon" viewBox="0 0 16 16" aria-hidden="true"><path d="M4 1h8v4H4zM1 6h14v6h-3v3H4v-3H1zM5 10v3h6v-3z"/></svg>
        +65 62418764
      </div>
      <div class="contact">
        <svg class="icon" viewBox="0 0 16 16" aria-hidden="true"><path d="M4 0h8a1 1 0 011 1v14a1 1 0 01-1 1H4a1 1 0 01-1-1V1a1 1 0 011-1zm1 2v10h6V2zm3 11a1 1 0 100 2 1 1 0 000-2z"/></svg>
        +65 9847 1156
      </div>
      <div class="contact">
        <svg class="icon" viewBox="0 0 16 16" aria-hidden="true"><path d="M1 3h14v10H1zm1.5 1.5v.3L8 9l5.5-4.2v-.3zM2.5 6.6v5h11v-5L8 10.8z"/></svg>
        marcus.teo@orbexfreight.example.sg
      </div>
    </div>

    <div class="address">
      <svg class="icon" viewBox="0 0 16 16" aria-hidden="true" style="width:16px;height:16px"><path d="M8 1l7 6.5h-2V15H9.5v-4h-3v4H3V7.5H1z"/></svg>
      14 Tuas Berry Industrial Way 3C #05-22 TBW Cargohub Singapore 539284
    </div>
  </section>

</body>
</html>
```